Lantern Newspaper needs a College Finder Flyer

Need an eye catching, information packed WHILE still ensuring all that is on the flyer is eye catching, lots of information that can be truncated or better said to shorten the info.. need it to be appealing to the eye. Great colors, bold and beautiful. We are doing our annual College guide, where thousands of students and adults will receive this for free. We are inviting colleges to advertise in this annual college guide I have attached a power point with the pertinent info.. please use your creative discretion as you see fit.. i would like an order form on the flyer as well maybe the bottom of the page i really cant figure out how to make it look good.. i ALSO need it to say somewhere about us (still need to type that up) looking for a draft right now with the info i do have ready and then it would just be one or two things i would need added - the about us and the order options

Target Market(s)

college marketing division

Industry/Entity Type

Advertising

Requirements
Must have
• clarity yet all the information i attached to the project
• i need a space to enter the about us part; i also need SOMEHOW for it to be known this is a newspaper that will be a college finder for all teens and adults in san Antonio- the college finder will be released twice with no additional payment required: 1st release- Oct 19, 2016 2nd release- Feb 22, 2017
• would like to let the audience know this is serving the majority of African-American and Hispanic Juniors and Seniors and Adults
Nice to have
• i leave the design up to the designer, but I'm looking for fresh-great eye catching colors-create the 'must have' feeling of the audience-
• please see attached power point with all the info i need in the flyer , feel free to re-word or say the same thing a different way!!! Use your creativeness- something which i do not have:)

```html
<!DOCTYPE html>
<html lang="en">
<head>
<meta charset="utf-8">
<title>Lantern Newspaper – College Guide Advertising Flyer</title>
<link rel="stylesheet" href="https://fonts.googleapis.com/css2?family=Oswald:wght@500;600;700&family=EB+Garamond:wght@400;700&display=swap">
<style>
  :root {
    --ink: #1f1f1f;
    --ink-soft: #3a3a3a;
    --yellow: #f5d10f;
    --yellow-deep: #e8b800;
    --red: #e1151b;
    --red-deep: #b80d12;
    --white: #ffffff;
    --green: #4f8a3a;
    --sans: "Oswald", "Arial Narrow", sans-serif;
    --serif: "EB Garamond", Georgia, serif;
  }
  * { margin: 0; padding: 0; box-sizing: border-box; }
  html, body { width: 907px; height: 1200px; overflow: hidden; background: #e6e6e6; }
  .flyer { position: relative; width: 907px; height: 1200px; overflow: hidden; font-family: var(--sans); }
  .backdrop { position: absolute; inset: 0; }
  .abs { position: absolute; }

  .brand-name { left: 49px; top: 24px; color: var(--yellow); font-weight: 700; font-size: 35px; letter-spacing: 0.5px; }
  .brand-city { left: 50px; top: 72px; color: var(--white); font-family: var(--serif); font-size: 36px; }

  .hero-photo {
    left: 465px; top: -170px; width: 560px; height: 560px; border-radius: 50%;
    background: radial-gradient(circle at 45% 60%, #7fa35a 0%, #4f7d38 45%, #2f5426 100%);
    border: 6px solid var(--white); box-shadow: 0 0 0 13px var(--red);
  }

  .invite { left: 49px; top: 150px; font-family: var(--serif); font-size: 31px; color: var(--ink); letter-spacing: 0.5px; }
  .headline { left: 44px; top: 186px; color: var(--red); font-weight: 700; font-size: 76px; line-height: 78px; letter-spacing: 0.5px; }

  .tab-label { color: var(--white); font-weight: 600; font-size: 27px; }
  .about-us-label { left: 44px; top: 375px; }
  .about-text { left: 44px; top: 433px; width: 826px; font-family: var(--serif); font-size: 13.6px; line-height: 18.8px; color: var(--ink); text-align: justify; }

  .feature { color: var(--white); font-weight: 500; font-size: 16.5px; line-height: 22px; text-align: justify; }
  .feature em { font-style: normal; color: var(--yellow); }
  .feature-reach { left: 39px; top: 588px; width: 343px; }
  .feature-military { left: 39px; top: 771px; width: 300px; }
  .feature-delivery { left: 39px; top: 954px; width: 254px; }

  .photo-badge { border-radius: 50%; border: 9px solid var(--yellow); }
  .badge-students { left: 396px; top: 572px; width: 176px; height: 176px; background: radial-gradient(circle, #f3c35a, #6fa6c9 70%, #3a6c8c); }
  .badge-military { left: 353px; top: 759px; width: 176px; height: 176px; background: radial-gradient(circle, #8a9bb5, #2c3850 70%, #1d2534); }
  .badge-delivery { left: 312px; top: 946px; width: 176px; height: 176px; background: var(--white); border-color: var(--yellow); box-shadow: inset 0 0 0 6px #d9d9d9; }

  .program-label { left: 640px; top: 578px; }
  .program-list { right: 32px; top: 638px; width: 400px; list-style: none; }
  .program-list li {
    position: relative; font-family: var(--serif); font-size: 16.5px; line-height: 22px;
    color: var(--white); text-align: right; padding-right: 25px; margin-bottom: 15px;
  }
  .program-list li::after {
    content: ""; position: absolute; right: 0; top: 4px; width: 12px; height: 12px;
    border-radius: 50%; background: var(--yellow);
  }

  .deadline { left: 34px; top: 1114px; color: var(--ink); font-weight: 600; font-size: 24px; }
  .deadline-date { left: 32px; top: 1143px; color: var(--red); font-family: var(--serif); font-weight: 700; font-size: 33px; }
  .contact { right: 35px; top: 1112px; text-align: right; color: var(--white); font-weight: 600; font-size: 22px; line-height: 34px; }
  .contact em { font-style: normal; color: var(--yellow); }
</style>
</head>
<body>
<div class="flyer">
  <svg class="backdrop" width="907" height="1200" viewBox="0 0 907 1200">
    <defs>
      <linearGradient id="yellowField" x1="0" y1="0" x2="1" y2="1">
        <stop offset="0" stop-color="#f8dd2a"/>
        <stop offset="0.6" stop-color="#f5d10f"/>
        <stop offset="1" stop-color="#e9bd05"/>
      </linearGradient>
      <linearGradient id="redField" x1="0" y1="0" x2="1" y2="1">
        <stop offset="0" stop-color="#b80d12"/>
        <stop offset="0.5" stop-color="#e1151b"/>
        <stop offset="1" stop-color="#c70f14"/>
      </linearGradient>
      <linearGradient id="darkField" x1="0" y1="0" x2="0" y2="1">
        <stop offset="0" stop-color="#2b2b2b"/>
        <stop offset="1" stop-color="#1c1c1c"/>
      </linearGradient>
    </defs>
    <!-- header band -->
    <rect x="0" y="0" width="907" height="128" fill="url(#darkField)"/>
    <rect x="0" y="128" width="907" height="8" fill="var(--red)"/>
    <!-- yellow field -->
    <rect x="0" y="136" width="907" height="414" fill="url(#yellowField)"/>
    <rect x="130" y="350" width="450" height="3" fill="#c99d00" opacity="0.6"/>
    <!-- about us tab -->
    <polygon points="0,370 260,370 282,418 0,418" fill="var(--ink)"/>
    <polygon points="262,370 270,370 292,418 284,418" fill="var(--white)"/>
    <!-- lower dark area -->
    <rect x="0" y="550" width="907" height="7" fill="var(--white)"/>
    <rect x="0" y="557" width="907" height="546" fill="url(#darkField)"/>
    <rect x="0" y="745" width="520" height="6" fill="var(--white)"/>
    <rect x="0" y="932" width="520" height="6" fill="var(--white)"/>
    <!-- red program panel -->
    <polygon points="493,557 505,557 421,1103 409,1103" fill="var(--white)"/>
    <polygon points="505,557 907,557 907,1103 421,1103" fill="url(#redField)"/>
    <!-- about program tab -->
    <polygon points="628,574 907,574 907,620 612,620" fill="var(--ink)"/>
    <polygon points="612,624 907,624 907,628 610,628" fill="var(--white)"/>
    <!-- bottom strip -->
    <rect x="0" y="1103" width="907" height="6" fill="var(--yellow)"/>
    <polygon points="0,1109 382,1109 356,1200 0,1200" fill="var(--white)"/>
    <polygon points="382,1109 396,1109 370,1200 356,1200" fill="var(--yellow)"/>
    <polygon points="396,1109 907,1109 907,1200 370,1200" fill="url(#darkField)"/>
  </svg>

  <div class="abs brand-name">PUBLISHING COMPANY</div>
  <div class="abs brand-city">San Antonio</div>

  <div class="abs hero-photo" role="img" aria-label="Photo of a group of young students jumping joyfully on a grassy lawn"></div>

  <div class="abs invite">INVITES YOU TO</div>
  <h1 class="abs headline">ADVERTISE<br>YOUR SCHOOL</h1>

  <div class="abs tab-label about-us-label">ABOUT US</div>
  <p class="abs about-text">Lorem ipsum dolor sit amet, consectetuer adipiscing elit. Aenean commodo ligula eget dolor. Aenean massa. Cum sociis natoquena et magnis dis parturient montes, nascetur ridiculus mus. Donec quam felis, ultricies nec, pellentesque eu, pretium quis, sem. Nulla consequat massa quis enim. Donec pede justo, fringilla vel, aliquet nec, vulputate eget, arcu. In enim justo, rhoncus ut, imperdiet a, enatis vitae, justo. Nullam dictum felis eu pede mollis pretium. Integer tincidunt. Cras dapibus. Vivamus elementum semper nisi. Aenean vulputate eleifend tellus. Aenean leo ligula, porttitor eu, consequat vitae, eleifend ac, enim.</p>

  <p class="abs feature feature-reach">Your school seen by over <em>20,000 JR &amp; SR</em> High School Students, 10,000 military (active duty and veterans) and over 40,000 adults who want to continue education utilizing <em>online programs</em>.</p>
  <p class="abs feature feature-military">Largest military populated city which includes <em>3 military bases</em>. You will reach all military branches and Wounded Warriors. This demographic has access to <em>VA and GI Bill Funding</em> to attend in person or online!</p>
  <p class="abs feature feature-delivery">This College Finder will be <em>FREE to all of the students, military, and adults and delivered</em> right to their hands! What a better way to know your school is being looked at!</p>

  <div class="abs photo-badge badge-students" role="img" aria-label="Photo of smiling teenage students giving thumbs up"></div>
  <div class="abs photo-badge badge-military" role="img" aria-label="Photo of uniformed military personnel marching"></div>
  <div class="abs photo-badge badge-delivery" role="img" aria-label="Illustration of a white delivery van marked free delivery"></div>

  <div class="abs tab-label program-label">ABOUT PROGRAM</div>
  <ul class="abs program-list">
    <li>The Publishing Company has<br>been in business for over 21<br>years in San Antonio<br>(7TH LARGEST city in the nation)</li>
    <li>The College Guide is FREE to the<br>students, military, and adults</li>
    <li>The College Guide will be jammed<br>packed with all about COLLEGE!<br>Don’t let your school miss out!</li>
    <li>TWO release dates for the price of<br>ONE AD (dates on following page)</li>
    <li>Pre-Pay and receive a 15% Discount! You may<br>also receive an invoice.</li>
    <li>All College Guides hand delivered to high<br>schools and military bases!</li>
    <li>Space is filling up get your order in today!</li>
  </ul>

  <div class="abs deadline">DAEDLINE FOR ART WORK</div>
  <div class="abs deadline-date">October 5, 2016</div>
  <div class="abs contact">Question? Call us <em>@ 210.555.0148</em><br>or email: <em>ads@lanternnews.com</em></div>
</div>
</body>
</html>
```